-Photo booth rental Web Design Project

Our business is a small photo booth rental service serving the capital region and surrounding areas. The photo booth is a portable booth that fits up to 10 guest. I am looking for a website that will have social media capabilities and also private log ins for clients to view their photo albums online after their event. We provide full service photo booth rentals for all types of parties. I am looking for something fun and unique but also professional and I am also looking to maybe somehow incorporate the age of the photo booth which was invented in 1888. I do not have the photos of our photo booth available because we are just starting up and I wanted to get everything together first but I will provide stock photo booth pictures .Thank you for your patience i know it wont be an easy task with out those things. I added a word document describing information i will need on our website, i am looking for a home page, contact us and book an event page, online gallery page, and pricing. If you need any more information please feel free to contact me. Thanks for your help and I look forward to working with you.

Target Market(s)

For everyone from brides to be for their weddings or private parties, corporate parties, school dances, charity events, community events ect

Industry/Entity Type

Business

Requirements
Nice to have
• social media sharing

```html
<!DOCTYPE html>
<html lang="en">
<head>
<meta charset="utf-8">
<title>Giddy Frames Photo Booth</title>
<link rel="stylesheet" href="https://fonts.googleapis.com/css2?family=Rye&family=Source+Sans+3:wght@300;400;600&display=swap">
<style>
:root{
  --page:#e1e1e1;
  --brown:#a08468;
  --brown-dark:#7b5b42;
  --ink-brown:#3d2517;
  --logo:#4a2c1c;
  --slider:#a9a9a9;
  --slider-edge:#cfcfcf;
  --text:#151515;
  --white:#ffffff;
  --rule:#6e5038;
}
*{margin:0;padding:0;box-sizing:border-box}
html,body{width:791px;height:1200px;overflow:hidden;background:var(--page)}
body{position:relative;font-family:"Source Sans 3",Arial,sans-serif;color:var(--text)}

.site-header{position:absolute;left:0;top:0;width:791px;height:168px}
.brand{position:absolute;left:24px;top:14px;color:var(--logo);font-weight:400;line-height:1}
.brand__name{display:block;font-size:64px;letter-spacing:-1.5px}
.brand__tag{display:block;font-size:58px;margin-left:118px;margin-top:-4px;letter-spacing:-1px}
.heritage{position:absolute;right:8px;top:92px;text-align:right;font-family:"Rye",Georgia,serif;color:var(--logo);font-size:21px;line-height:27px}

.main-nav{position:absolute;left:0;top:168px;width:791px;height:32px;background:var(--brown)}
.main-nav a{position:absolute;top:0;height:32px;line-height:32px;font-size:24px;font-weight:300;color:var(--ink-brown);text-decoration:none;text-transform:uppercase}
.main-nav a.is-active{background:var(--brown-dark);padding:0 10px}

.intro-title{position:absolute;left:0;top:244px;width:791px;text-align:center;white-space:nowrap;font-weight:400}
.intro-title span{display:inline-block;font-family:"Rye",Georgia,serif;font-size:28px;line-height:34px;color:#111;transform:scaleX(.7);transform-origin:center}

.slider{position:absolute;left:22px;top:300px;width:746px;height:331px;background:var(--slider);border:3px solid var(--slider-edge)}
.slide{position:absolute}
.slide--side-left{left:54px;top:70px;width:94px;height:192px;background:linear-gradient(160deg,#6a6a6a,#3d3d3d)}
.slide--side-right{left:600px;top:70px;width:90px;height:192px;background:linear-gradient(200deg,#6a6a6a,#3d3d3d)}
.slide--current{left:148px;top:11px;width:454px;height:303px;background:linear-gradient(90deg,#e9e9e9 0%,#d6d6d6 45%,#c9c9c9 70%,#e6e6e6 100%)}
.slider__arrow{position:absolute;top:134px;width:64px;height:58px;background:rgba(200,200,200,.55);display:flex;align-items:center;justify-content:center}
.slider__arrow--prev{left:5px}
.slider__arrow--next{right:5px}
.slider__dots{position:absolute;left:265px;top:290px;display:flex;gap:15px}
.slider__dots span{width:16px;height:16px;border-radius:50%;background:#9a9a9a}
.slider__dots span.is-current{background:#5c5c5c}

.intro-copy{position:absolute;left:11px;top:662px;width:748px;font-size:26px;line-height:30px;font-weight:400}
.intro-copy p+p{margin-top:30px}

.site-footer{position:absolute;left:0;top:958px;width:791px;height:242px;background:var(--brown);border-top:3px solid var(--rule);color:var(--white)}
.footer-col__title{font-size:25px;font-weight:400}
.quick-links{position:absolute;left:25px;top:20px}
.quick-links ul{list-style:none;margin-left:19px;margin-top:2px}
.quick-links li{font-size:22px;line-height:29px;width:101px;border-bottom:1px solid #c2a88c}
.quick-links a{color:var(--white);text-decoration:none}
.footer-divider{position:absolute;top:55px;width:2px;height:178px;background:#8a6d52}
.contact{position:absolute;left:291px;top:20px}
.contact__list{list-style:none;margin-top:10px}
.contact__company{font-size:23px;margin-left:17px}
.contact__row{display:flex;align-items:flex-start;gap:8px;font-size:22px;line-height:28px;margin-top:4px}
.contact__row svg{flex:none;margin-top:2px}
.follow{position:absolute;left:586px;top:20px;width:200px;text-align:center}
.follow__list{list-style:none;display:grid;grid-template-columns:1fr 1fr;row-gap:30px;margin-top:22px;justify-items:center}
.follow__list li{font-size:18px;font-weight:600;color:var(--ink-brown);display:flex;align-items:center;gap:4px;white-space:nowrap}
.follow__list li i{display:block;width:12px;height:12px;background:var(--ink-brown)}
.copyright{position:absolute;right:8px;bottom:4px;font-size:15px;color:var(--white)}
</style>
</head>
<body>

<header class="site-header">
  <div class="brand">
    <span class="brand__name">Giddy Frames</span>
    <span class="brand__tag">photo booth</span>
  </div>
  <p class="heritage">PHOTO BOOTHS<br>SINCE 1888</p>
</header>

<nav class="main-nav">
  <a href="#" class="is-active" style="left:3px">Home</a>
  <a href="#" style="left:116px">About</a>
  <a href="#" style="left:230px">Pricing</a>
  <a href="#" style="left:357px">Book an event</a>
  <a href="#" style="left:567px">Contact</a>
  <a href="#" style="left:702px">Log-in</a>
</nav>

<h1 class="intro-title"><span>WE HAVE THE RIGHT PHOTO BOOTH FOT YOUR EVENT</span></h1>

<section class="slider">
  <div class="slide slide--side-left" role="img" aria-label="Guest in a masquerade mask posing in the photo booth"></div>
  <div class="slide slide--side-right" role="img" aria-label="Guest with glasses and moustache prop in the photo booth"></div>
  <div class="slide slide--current" role="img" aria-label="Bride and groom posing with party props in front of a height chart backdrop"></div>
  <div class="slider__arrow slider__arrow--prev">
    <svg width="26" height="46" viewBox="0 0 26 46"><polyline points="23,2 3,23 23,44" fill="none" stroke="#333" stroke-width="3"/></svg>
  </div>
  <div class="slider__arrow slider__arrow--next">
    <svg width="26" height="46" viewBox="0 0 26 46"><polyline points="3,2 23,23 3,44" fill="none" stroke="#333" stroke-width="3"/></svg>
  </div>
  <div class="slider__dots">
    <span class="is-current"></span><span></span><span></span><span></span><span></span><span></span><span></span>
  </div>
</section>

<section class="intro-copy">
  <p>We have photo booths that fit up to ten people. They are very suitable for birthdays, weddings or company events. For details on the options on different packages, please see the Pricing page.</p>
  <p>If you have questions or suggestions about anything, don’t hesitate and let us know.</p>
</section>

<footer class="site-footer">
  <div class="quick-links">
    <h2 class="footer-col__title">Quick links</h2>
    <ul>
      <li><a href="#">&gt; Home</a></li>
      <li><a href="#">&gt; About</a></li>
      <li><a href="#">&gt; Pricing</a></li>
      <li><a href="#" style="white-space:nowrap">&gt; Book an event</a></li>
      <li><a href="#">&gt; Contact</a></li>
      <li><a href="#">&gt; Log-in</a></li>
    </ul>
  </div>
  <div class="footer-divider" style="left:240px"></div>

  <div class="contact">
    <h2 class="footer-col__title">Contact details</h2>
    <ul class="contact__list">
      <li class="contact__company">Giddy Frames Photo Booth</li>
      <li class="contact__row">
        <svg width="26" height="26" viewBox="0 0 26 26"><path d="M13 2 1 13h4v11h6v-7h4v7h6V13h4z" fill="#111"/></svg>
        <span>482 Lantern Road<br>Albany, NY 12207</span>
      </li>
      <li class="contact__row">
        <svg width="26" height="26" viewBox="0 0 26 26"><path d="M6 2c1 0 2 .5 2.5 1.5l2 4c.3.8 0 1.6-.6 2.1L8 11c1.3 3 3.7 5.4 7 7l1.4-1.9c.5-.6 1.3-.9 2.1-.6l4 2c1 .5 1.5 1.5 1.5 2.5 0 2.5-2 4-4 4C10 24 2 16 2 6c0-2 1.5-4 4-4z" fill="#111"/></svg>
        <span>(518)-555-0142</span>
      </li>
      <li class="contact__row">
        <svg width="28" height="22" viewBox="0 0 28 22"><rect x="1.5" y="1.5" width="25" height="19" fill="none" stroke="#111" stroke-width="2"/><polyline points="1.5,1.5 14,12 26.5,1.5" fill="none" stroke="#111" stroke-width="2"/><line x1="1.5" y1="20.5" x2="11" y2="10" stroke="#111" stroke-width="2"/><line x1="26.5" y1="20.5" x2="17" y2="10" stroke="#111" stroke-width="2"/></svg>
        <span>hello@giddyframes.com</span>
      </li>
    </ul>
  </div>
  <div class="footer-divider" style="left:580px"></div>

  <div class="follow">
    <h2 class="footer-col__title">Follow us</h2>
    <ul class="follow__list">
      <li><i></i>Friendly</li>
      <li><i></i>Chirper</li>
      <li><i></i>Pixgram</li>
      <li><i></i>ClipTube</li>
    </ul>
  </div>

  <p class="copyright">© 2014 Giddy Frames Photo Booth</p>
</footer>

</body>
</html>
```